Flyer-Design für Brick and Stone Restorator
Zielgruppe
Wir sind Sydneys führender Brick and Stone Restorator.
Aufgabenstellung
Unsere neue webseite geht in ein paar tagen online und wir möchten gerne passenden zur neuen Webseite ein corporate Flyer, letztendlich soll es ein Print Version von unserer neuen Webseite sein. Sprich die wichtigsten Informationen der Webseite soll in dem Flyer enthalten sein. Letztendlich möchte ich designer keine großen einschränkungen geben, weil das ist euer job kreativ sein ;), aber der flyer sollte evtl. so aufgebaut sein das am Ende die leute entweder uns anrufen oder doch auf unsere neue Webseite gehen sprich evtl ein QR- code or what ever.
Unsere Domain ist kestrelvale.com.au, aber damit ihr die neue Webseite schon sehen könnt müsst ihr auf kestrelvale.com.au/ new, falls dieser Link nicht mehr funktionieren sollte, ist sie schon auf der richtigen domain hochgeladen.
Falls ihr irgendwelche Logos Bilder oder sonst was benötigt und diese nicht aus der Webseite entnehmen könnt, schickt einfach eine kurze Naricht, ich beantworte diese so schnell wie möglich ;)
der Flyer soll ein 6 pager sein!!
mit freundlichen Grüßen euer Kestrel Vale Team

```html
<!DOCTYPE html>
<html lang="en">
<head>
<meta charset="utf-8">
<title>Kestrel Vale – Brick and Stone Restoration Brochure</title>
<link rel="stylesheet" href="https://fonts.googleapis.com/css2?family=Montserrat:wght@400;500;600&family=Quicksand:wght@400;500&display=swap">
<style>
  :root{
    --plum:#352a4f;
    --sand:#d8ceb4;
    --paper:#ffffff;
    --ink:#2c2440;
    --brick:#8a3f2c;
    --brick-dark:#5a2a22;
    --stone:#5b5650;
    --sky:#9fc3e6;
  }
  *{box-sizing:border-box;margin:0;padding:0}
  html,body{width:1150px;height:1200px;overflow:hidden;background:var(--paper)}
  body{position:relative;font-family:"Montserrat",Arial,sans-serif;color:var(--ink)}
  .spread{position:absolute;left:58px;width:1034px;height:517px;background:var(--paper);overflow:hidden;box-shadow:0 2px 6px rgba(0,0,0,.25)}
  .spread--outside{top:50px}
  .spread--inside{top:613px}
  .spread svg.shapes{position:absolute;inset:0;width:1034px;height:517px}
  .photo{position:absolute}
  .abs{position:absolute}
  .heading{font-family:"Quicksand",Arial,sans-serif;font-weight:400;line-height:1.05}
  .heading--light{color:#fff;font-size:14px}
  .heading--dark{color:var(--ink);font-size:20px}
  .body-copy{font-size:6.6px;line-height:9.4px;text-align:justify;color:#fff}
  .body-copy p+p{margin-top:7px}
  .service-list{list-style:none;font-size:6.6px;line-height:9.2px;font-weight:600;color:#fff}
  .contact-intro{font-size:8.6px;line-height:12px;color:#fff}
  .contact-row{display:flex;align-items:center;gap:10px;font-size:8.6px;line-height:11px;color:#fff}
  .contact-icon{width:26px;height:26px;flex:none}
  .licence{font-size:8px;color:#cfc9dc}
  .brand{text-align:center;color:var(--plum)}
  .brand__name{font-family:"Montserrat",Arial,sans-serif;font-weight:600;font-size:30px;letter-spacing:1px;line-height:1}
  .brand__tag{font-family:"Montserrat",Arial,sans-serif;font-weight:600;font-size:8.6px;letter-spacing:1px;margin-top:8px}
  .info-box{background:var(--plum);color:#fff;padding:10px 12px}
  .info-box h3{font-size:9px;font-weight:500;text-decoration:underline;margin-bottom:7px;letter-spacing:.2px}
  .info-box ul{list-style:none;font-size:6.8px;line-height:8.6px}
  .info-box ol{font-size:6.8px;line-height:8.6px;padding-left:10px}
  .info-box ol li{margin-bottom:7px}
  .info-box p{font-size:6.8px;line-height:8.6px}
  .side-note{font-family:"Quicksand",Arial,sans-serif;font-size:10.4px;line-height:14px;color:var(--ink)}
</style>
</head>
<body>

<!-- Outside spread: philosophy / contact / cover -->
<section class="spread spread--outside" aria-label="Brochure outside spread">
  <div class="photo" style="left:0;top:0;width:345px;height:270px;background:linear-gradient(180deg,#3f7a3a 0%,#4e8a45 28%,#7a3a2c 40%,#5c2e26 100%)" role="img" aria-label="Photo of a restored red and blue brick garden wall with hedge behind"></div>
  <div class="photo" style="left:345px;top:0;width:345px;height:360px;background:linear-gradient(135deg,#8a3f2c 0%,#9b4a33 45%,#6d3328 100%)" role="img" aria-label="Photo of a red brick facade with arched barred windows"></div>
  <div class="photo" style="left:690px;top:0;width:344px;height:360px;background:linear-gradient(180deg,#b6d3ef 0%,#7d8a96 25%,#4e4a46 60%,#6b5f52 100%)" role="img" aria-label="Photo of a gothic bluestone church facade with sandstone arch"></div>

  <svg class="shapes" viewBox="0 0 1034 517" aria-hidden="true">
    <polygon points="0,215 120,186 345,186 345,517 0,517" fill="#352a4f"/>
    <polygon points="0,215 120,186 0,196" fill="#ffffff"/>
    <polygon points="0,300 345,372 345,388 0,318" fill="#d8ceb4"/>
    <polygon points="345,360 690,360 690,386 430,386 345,376" fill="#ffffff"/>
    <polygon points="345,386 520,345 690,330 690,517 345,517" fill="#352a4f"/>
    <polygon points="520,345 690,292 690,330" fill="#d8ceb4"/>
    <polygon points="690,330 690,360 1034,360 1034,517 690,517" fill="#ffffff"/>
    <polygon points="690,330 760,300 1034,300 1034,360" fill="#ffffff"/>
    <polygon points="830,365 1034,298 1034,350 900,365" fill="#352a4f"/>
    <polygon points="690,330 830,365 690,360" fill="#d8ceb4"/>
  </svg>

  <h2 class="abs heading heading--light" style="left:26px;top:210px">The Kestrel Vale philosophy</h2>
  <div class="abs body-copy" style="left:26px;top:234px;width:292px">
    <p>Bricks and mortar are the foundation of your home or building. Not only do you want a structurally strong and sound building, you also want the building's integrity and historic character upheld and protected for years to come. This is exactly what the talented craftsmen at Kestrel Vale believe and strive to achieve on each and every job they commit to. If you want the best brick pointing in Sydney, pick up the phone.</p>
  </div>

  <h2 class="abs heading heading--light" style="left:26px;top:360px">Why choose us?</h2>
  <div class="abs body-copy" style="left:26px;top:384px;width:292px">
    <p>Maintaining the bricks and mortar of your building in premium condition is about more than protecting the overall health of your building's structure – it's a complete investment in your building's future.</p>
    <p>It's easy to return your building to its former glory with Kestrel Vale's complete range of brick repointing services including:</p>
  </div>
  <ul class="abs service-list" style="left:26px;top:460px">
    <li>» Stone &amp; brick repointing</li>
    <li>» Tuckpointing</li>
    <li>» Brick restoration &amp; repair</li>
    <li>» Brick staining</li>
  </ul>
  <ul class="abs service-list" style="left:157px;top:460px">
    <li>» Wall tie replacement</li>
    <li>» Arch-bar replacement</li>
    <li>» Water repellent and brick sealing solutions</li>
    <li>» Heritage projects</li>
  </ul>

  <p class="abs contact-intro" style="left:434px;top:364px;width:220px">Kestrel Vale are located in Sydney's Eastern Suburbs and cater to all areas.</p>
  <div class="abs contact-row" style="left:434px;top:394px">
    <svg class="contact-icon" viewBox="0 0 26 26" aria-hidden="true"><circle cx="13" cy="13" r="12.5" fill="#fff"/><path d="M6.5 13 13 7.5 19.5 13h-2v5.5h-3.2v-3.6h-2.6v3.6H8.5V13z" fill="#352a4f"/></svg>
    <span>PO Box 4821, Coogee,<br>NSW 2034</span>
  </div>
  <div class="abs contact-row" style="left:434px;top:428px">
    <svg class="contact-icon" viewBox="0 0 26 26" aria-hidden="true"><circle cx="13" cy="13" r="12.5" fill="#fff"/><path d="M9.2 7.2c.6-.4 1.3-.3 1.7.3l1.3 2c.3.5.2 1.1-.2 1.5l-.8.7c.6 1.4 1.7 2.6 3.1 3.3l.8-.8c.4-.4 1-.5 1.5-.2l2 1.2c.6.4.8 1.1.4 1.7l-.7 1.1c-.5.8-1.5 1.1-2.4.8-3.5-1.2-6.2-3.9-7.4-7.4-.3-.9 0-1.9.8-2.4z" fill="#352a4f"/></svg>
    <span>Office phone: 0400 555 017</span>
  </div>
  <div class="abs contact-row" style="left:434px;top:459px">
    <svg class="contact-icon" viewBox="0 0 26 26" aria-hidden="true"><circle cx="13" cy="13" r="12.5" fill="#fff"/><g fill="none" stroke="#352a4f" stroke-width="1.1"><circle cx="13" cy="13" r="6.5"/><ellipse cx="13" cy="13" rx="3" ry="6.5"/><path d="M6.5 13h13M7.6 9.6h10.8M7.6 16.4h10.8"/></g></svg>
    <span>www.kestrelvale.com.au</span>
  </div>
  <p class="abs licence" style="left:434px;top:494px">Licence no: 481736D</p>

  <div class="abs brand" style="left:800px;top:422px;width:236px">
    <div class="brand__name">KESTREL VALE</div>
    <div class="brand__tag">BRICK AND STONE RESTORATION</div>
  </div>
</section>

<!-- Inside spread: heritage / residential / decorative -->
<section class="spread spread--inside" aria-label="Brochure inside spread">
  <div class="photo" style="left:0;top:0;width:329px;height:190px;background:linear-gradient(180deg,#9a5a44 0%,#b7735a 40%,#c9b8a8 100%)" role="img" aria-label="Photo of a heritage brick building with scaffolding during restoration"></div>
  <div class="photo" style="left:0;top:359px;width:329px;height:158px;background:linear-gradient(135deg,#8e3f2e 0%,#a75239 50%,#d9d2c4 100%)" role="img" aria-label="Photo of a heritage brick entrance and memorial honour board"></div>
  <div class="photo" style="left:363px;top:0;width:311px;height:215px;background:linear-gradient(180deg,#7fb0de 0%,#6b3328 22%,#7b3b2d 100%)" role="img" aria-label="Photo of a three-storey red brick apartment block"></div>
  <div class="photo" style="left:708px;top:268px;width:326px;height:249px;background:linear-gradient(135deg,#6f8a5a 0%,#8c3a2c 30%,#9d4531 75%,#7a2e25 100%)" role="img" aria-label="Photo of a restored red brick residential home with timber door"></div>

  <svg class="shapes" viewBox="0 0 1034 517" aria-hidden="true">
    <polygon points="0,170 329,200 329,215 0,190" fill="#ffffff"/>
    <polygon points="0,172 345,224 345,234 0,185" fill="#d8ceb4"/>
    <polygon points="345,210 674,210 674,230 345,250" fill="#352a4f"/>
    <polygon points="345,250 560,208 690,236 690,250" fill="#d8ceb4"/>
    <polygon points="345,252 560,214 690,242 690,262 345,262" fill="#ffffff"/>
    <polygon points="708,300 820,285 1034,262 1034,268 708,268" fill="#ffffff"/>
    <polygon points="820,290 1034,268 1034,276 880,292" fill="#d8ceb4"/>
  </svg>

  <h2 class="abs heading heading--dark" style="left:24px;top:210px">Heritage Brick<br>Restoration</h2>
  <div class="abs info-box" style="left:0;top:253px;width:206px;height:164px;padding-left:26px">
    <h3>HERITAGE WORKS INCLUDE:</h3>
    <ul>
      <li>» Stone and brick façade restoration</li>
      <li>» Structural repair</li>
      <li>» Heritage Brick Restoration</li>
      <li>» Repointing</li>
      <li>» Tuckpointing (white or black line)</li>
      <li>» Damp issues (Kestrel Vale uses waterproofing products from heritage experts – Harlow Remedial)</li>
      <li>» Specially formulated heritage mortar (Kestrel Vale uses the highest quality mortar products developed by heritage brick restoration experts – Corvane)</li>
    </ul>
  </div>
  <p class="abs side-note" style="left:221px;top:260px;width:118px">The Kestrel Vale team have accomplished restoration works for heritage buildings throughout NSW.</p>

  <h2 class="abs heading heading--dark" style="left:363px;top:270px;font-size:21px">Residental bricks<br>and stone restoration</h2>
  <div class="abs info-box" style="left:365px;top:312px;width:309px;height:205px;padding:12px 12px 10px 20px">
    <h3>REPOINTING</h3>
    <p>What is repointing? Repointing is an intricate process requiring a high level of proficiency and experience to ensure the integrity of your building is upheld.</p>
    <p style="margin:10px 0 7px">The repointing process:</p>
    <ol>
      <li>Decayed mortar is carefully raked out of the brick or stone joints and the joints are then washed to remove any dust and debris</li>
      <li>Depending on your building, Kestrel Vale will inspect the original joint and mortar type – creating a new mortar closely matching the original colour and texture</li>
      <li>Mortar is injected into the joint, with careful consideration taken to ensure the original joint profile is correct</li>
      <li>Once the mortar is dry, your brickwork is thoroughly cleaned with a high-pressure water brick cleaning system</li>
    </ol>
  </div>

  <h2 class="abs heading heading--dark" style="left:707px;top:26px;font-size:21px">Decorative Brick<br>&amp; Stone finishes</h2>
  <div class="abs info-box body-copy" style="left:709px;top:73px;width:325px;height:163px;padding:12px 14px 10px 16px">
    <p>If you're an owner of a brick home or building, you could be faced with brickwork problems that result in disrepair, crumbling or collapse. When reversing the damage to your stone or brickwork you'll want to ensure your building is restored safely, while maintaining its original character and integrity. Your home or heritage building may be experiencing fretting, bowed or loose brickwork. Once this process starts it can potentially lead to cracks on the outside of the brickwork, ultimately requiring extensive mortar and brick repair.</p>
    <p>If your home or heritage building is located in Sydney, it's more than likely that your building is experiencing a high occurrence of salt intolerance. Salt crystals can stick to the surface of your brickwork, gradually eating away at the structure and causing deterioration. Restore your building and prevent further damage with Kestrel Vale's water repellent products and brick sealing solutions, which can be applied to prevent further infiltration of water.</p>
  </div>
</section>

</body>
</html>
```